redesign of one of my packaging

Here I have a product packaging design that I have been using for a while on my e-commerce platform. I am planning on having multiple products very soon so I would like to have a packaging design that I will use for all my products that will represent my brand.
This is a zero-waste, eco-friendly/ sustainable product brand.
The packaging design that I use now needs to be redesign to match my brand a bit more.

-So in the file, you can find my current packaging design, All the text on the packaging is accurate the only thing is the brand name(logo) has been changed as well as the email address. I will put in the file the new brand name logo and the new email is "kestilo@fernwix.com" for detail ( Refer to pic #1)
(I am very open to the text I have. It doesn't have to be all there and if it is then the location of all the text is your choice)

- I currently have a designer that is modifying my packaging design. He is very good at designing and the design he sent me are nice but I need more different option to choose from. Here I will attach the design he got me so far. (refer to pic#2)

-For the design, I am very open to any kind of design. The only thing I want is to have the most of the background with the natural packaging color. For a sample of the color of my packaging (refer to pic#3)

-For the color... I would like for the design to have the 2 colors of my logo(blue and green)
but this is the first product of the line so I would not mind having the color of the logo different to have a better fit with the design of the packaging.

WHAT I LIKE:
-I like the concept of the bottom or top of the packaging when its a plain bright color
-I like when the packaging is not to busy in writing or shape
-I like to have an eco-friendly sign like the one on the current packaging
-I like little plain design but with nice little detail into it
-I like the color of my logo to be on the packaging(color of the logo can be modified)
-I like the contrast of the white on the natural color of the packaging
- I like the shade of all the item of the product on the bottom part of the current design( Not a need. Refer to pic#4)

What I like does, not mean that it needs to be on the design, I am very open to any design.

So I will also put in the files section some pictures of existing packaging design that I really like. Just to give you a good idea of what I want.
Those picture name will be (Design idea)

I will also put a picture of the actual product to help you with the design creation. The file name will be (Bamboo cutlery set)

Looking forward to seeing your design and I thank you in advance.

Theodore

```html
<!DOCTYPE html>
<html lang="en">
<head>
<meta charset="utf-8">
<title>Organic Bamboo Cutlery Set – Packaging Panels</title>
<link rel="stylesheet" href="https://fonts.googleapis.com/css2?family=Baloo+2:wght@600;700&family=Montserrat:wght@300;400;500;600&display=swap">
<style>
  :root {
    --kraft: #a88d69;
    --kraft-dark: #8f7553;
    --leaf-green: #8dc63f;
    --teal: #16a996;
    --teal-deep: #0e8f80;
    --white: #ffffff;
    --ink: #3b2f22;
    --page: #ffffff;
  }
  * { box-sizing: border-box; margin: 0; padding: 0; }
  html, body { width: 1200px; height: 1200px; overflow: hidden; background: var(--page); }
  .canvas { position: relative; width: 1200px; height: 1200px; }

  .dieline {
    position: absolute; left: 260px; top: 60px;
    display: flex; height: 1080px;
    box-shadow: 0 6px 24px rgba(0,0,0,.12);
  }
  .panel {
    position: relative; height: 100%;
    background: var(--kraft);
    border-right: 1px solid var(--kraft-dark);
    overflow: hidden;
  }
  .panel:last-child { border-right: none; }
  .panel--side { width: 135px; }
  .panel--front { width: 205px; }

  .header-band {
    position: absolute; top: 0; left: 0; right: 0; height: 170px;
  }
  .header-band svg { position: absolute; inset: 0; width: 100%; height: 100%; }
  .header-title {
    position: absolute; top: 24px; left: 0; right: 0;
    text-align: center;
    font-family: "Baloo 2", sans-serif; font-weight: 700;
    color: var(--white); line-height: 1.02;
  }
  .panel--front .header-title { font-size: 26px; }
  .panel--side .header-title { font-size: 19px; }
  .header-title .title-accent { color: var(--teal-deep); font-size: 1.25em; display: block; }

  .brand-name {
    position: absolute; top: 300px; left: 0; right: 0;
    text-align: center;
    font-family: "Baloo 2", sans-serif; font-weight: 700;
    font-size: 34px; color: var(--teal-deep);
  }

  .eco-badge {
    position: absolute; top: 190px; left: 50%; transform: translateX(-50%);
    width: 70px; height: 70px; border-radius: 50%;
    background: var(--leaf-green); border: 4px solid var(--teal);
  }
  .maker {
    position: absolute; top: 280px; left: 0; right: 0; text-align: center;
    font-family: "Montserrat", sans-serif; color: var(--ink);
  }
  .maker-label { font-size: 10px; font-weight: 400; }
  .maker-name { font-size: 15px; font-weight: 600; margin-top: 2px; }
  .maker-email {
    margin-top: 14px; font-size: 9px; display: flex; align-items: center; justify-content: center; gap: 4px;
  }
  .maker-email svg { width: 10px; height: 8px; }
  .origin {
    position: absolute; top: 700px; left: 0; right: 0; text-align: center;
    font-family: "Montserrat", sans-serif; font-size: 8px; color: var(--ink); line-height: 1.5;
  }

  .inside-title {
    position: absolute; top: 180px; left: 0; right: 0; text-align: center;
    font-family: "Baloo 2", sans-serif; font-weight: 600; font-size: 15px;
    color: var(--teal); text-decoration: underline;
  }
  .inside-frame {
    position: absolute; top: 204px; left: 27px; width: 81px; height: 470px;
    border: 2px solid var(--teal);
    display: flex; flex-direction: column; justify-content: space-around; align-items: center;
    padding: 8px 4px; list-style: none;
  }
  .item { display: flex; flex-direction: column; align-items: center; gap: 4px; }
  .item-shape { width: 66px; height: 9px; background: var(--white); border-radius: 5px; }
  .item-shape--case { height: 22px; border-radius: 4px; }
  .item-size { font-family: "Montserrat", sans-serif; font-size: 6px; color: var(--white); white-space: nowrap; }

  .claims {
    position: absolute; top: 204px; height: 470px;
    font-family: "Montserrat", sans-serif; font-size: 9px; color: var(--ink);
    display: flex; justify-content: space-between; align-items: center;
    writing-mode: vertical-rl;
  }
  .claims--left { left: 6px; transform: rotate(180deg); }
  .claims--right { right: 6px; }
  .claims .sep { width: 4px; height: 4px; background: var(--ink); display: inline-block; }

  .inside-note {
    position: absolute; top: 682px; left: 0; right: 0; text-align: center;
    font-family: "Montserrat", sans-serif; font-weight: 500; font-size: 7px;
    color: var(--leaf-green); line-height: 1.4; white-space: nowrap;
  }

  .bamboo-field {
    position: absolute; left: 0; right: 0; bottom: 0; height: 300px;
  }
  .bamboo-field svg { width: 100%; height: 100%; display: block; }
</style>
</head>
<body>
<main class="canvas">
  <div class="dieline">

    <!-- Side panel: maker details -->
    <section class="panel panel--side">
      <div class="header-band">
        <svg viewBox="0 0 135 170" preserveAspectRatio="none" aria-hidden="true">
          <path d="M0 0H135V138Q67 128 0 142Z" fill="var(--leaf-green)"/>
          <path d="M0 142Q67 128 135 138V162Q67 150 0 166Z" fill="var(--teal)"/>
        </svg>
        <h2 class="header-title">100% Organic<br>Bambo<span class="title-accent">Cutlery Set</span></h2>
      </div>
      <div class="eco-badge" role="img" aria-label="Eco-friendly badge"></div>
      <div class="maker">
        <p class="maker-label">Manufactured by</p>
        <p class="maker-name">Verdalo</p>
        <p class="maker-email">
          <svg viewBox="0 0 10 8" aria-hidden="true"><rect x=".5" y=".5" width="9" height="7" fill="none" stroke="var(--ink)"/><path d="M.5 .5L5 4.5 9.5 .5" fill="none" stroke="var(--ink)"/></svg>
          kestilo@fernwix.com
        </p>
      </div>
      <p class="origin">Bamboo Reusable Cutlery Set<br>New<br>Made in China</p>
      <div class="bamboo-field">
        <svg viewBox="0 0 135 300" preserveAspectRatio="none" role="img" aria-label="Bamboo stalks with cutlery silhouettes rising among leaves">
          <defs><linearGradient id="fieldA" x1="0" y1="0" x2="0" y2="1"><stop offset="0" stop-color="var(--teal)" stop-opacity="0"/><stop offset=".45" stop-color="var(--teal)"/><stop offset="1" stop-color="var(--teal)"/></linearGradient></defs>
          <rect width="135" height="300" fill="url(#fieldA)"/>
        </svg>
      </div>
    </section>

    <!-- Front panel -->
    <section class="panel panel--front">
      <div class="header-band">
        <svg viewBox="0 0 205 170" preserveAspectRatio="none" aria-hidden="true">
          <path d="M0 0H205V134Q102 126 0 140Z" fill="var(--leaf-green)"/>
          <path d="M0 140Q102 126 205 134V160Q102 148 0 166Z" fill="var(--teal)"/>
        </svg>
        <h1 class="header-title">100% Organic<br>Bambo<span class="title-accent">Cutlery Set</span></h1>
      </div>
      <p class="brand-name">Verdalo</p>
      <div class="bamboo-field">
        <svg viewBox="0 0 205 300" preserveAspectRatio="none" role="img" aria-label="Bamboo stalks with cutlery silhouettes rising among leaves">
          <defs><linearGradient id="fieldB" x1="0" y1="0" x2="0" y2="1"><stop offset="0" stop-color="var(--teal)" stop-opacity="0"/><stop offset=".45" stop-color="var(--teal)"/><stop offset="1" stop-color="var(--teal)"/></linearGradient></defs>
          <rect width="205" height="300" fill="url(#fieldB)"/>
        </svg>
      </div>
    </section>

    <!-- Side panel: what's inside -->
    <section class="panel panel--side">
      <div class="header-band">
        <svg viewBox="0 0 135 170" preserveAspectRatio="none" aria-hidden="true">
          <path d="M0 0H135V138Q67 128 0 142Z" fill="var(--leaf-green)"/>
          <path d="M0 142Q67 128 135 138V162Q67 150 0 166Z" fill="var(--teal)"/>
        </svg>
        <h2 class="header-title">100% Organic<br>Bambo<span class="title-accent">Cutlery Set</span></h2>
      </div>
      <p class="inside-title">Whats Inside?</p>
      <div class="claims claims--left">
        <span>Made from Natural Bamboo</span><span class="sep"></span>
        <span>Highly Durable</span><span class="sep"></span>
        <span>Super Sustainable</span>
      </div>
      <ul class="inside-frame">
        <li class="item"><span class="item-shape item-shape--case" role="img" aria-label="Carry case"></span><span class="item-size">A: 8.1 inch - B: 1.4 inch</span></li>
        <li class="item"><span class="item-shape" role="img" aria-label="Spoon"></span><span class="item-size">A: 7.5 inch - B: 1.2 inch</span></li>
        <li class="item"><span class="item-shape" role="img" aria-label="Fork"></span><span class="item-size">A: 7.5 inch - B: 1.2 inch</span></li>
        <li class="item"><span class="item-shape" role="img" aria-label="Chopsticks"></span><span class="item-size">A: 7.5 inch - B: 0.9 inch</span></li>
        <li class="item"><span class="item-shape" role="img" aria-label="Knife"></span><span class="item-size">A: 7.5 inch - B: 0.4 inch</span></li>
        <li class="item"><span class="item-shape" role="img" aria-label="Straw and cleaning brush"></span><span class="item-size">A: 7.5 inch - B: 0.3 inch</span></li>
        <li class="item"><span class="item-shape" role="img" aria-label="Toothbrush"></span><span class="item-size">A: 6.9 inch - B: 0.7 inch</span></li>
      </ul>
      <div class="claims claims--right">
        <span>Easy to Use and Clean</span><span class="sep"></span>
        <span>Hand Finished</span><span class="sep"></span>
        <span>Lightweight</span>
      </div>
      <p class="inside-note">With chopstick, toothbrush,<br>bamboo straw &amp; cleaning brush</p>
      <div class="bamboo-field">
        <svg viewBox="0 0 135 300" preserveAspectRatio="none" role="img" aria-label="Bamboo stalks with cutlery silhouettes rising among leaves">
          <defs><linearGradient id="fieldC" x1="0" y1="0" x2="0" y2="1"><stop offset="0" stop-color="var(--teal)" stop-opacity="0"/><stop offset=".45" stop-color="var(--teal)"/><stop offset="1" stop-color="var(--teal)"/></linearGradient></defs>
          <rect width="135" height="300" fill="url(#fieldC)"/>
        </svg>
      </div>
    </section>

    <!-- Back panel -->
    <section class="panel panel--front">
      <div class="header-band">
        <svg viewBox="0 0 205 170" preserveAspectRatio="none" aria-hidden="true">
          <path d="M0 0H205V134Q102 126 0 140Z" fill="var(--leaf-green)"/>
          <path d="M0 140Q102 126 205 134V160Q102 148 0 166Z" fill="var(--teal)"/>
        </svg>
        <h2 class="header-title">100% Organic<br>Bambo<span class="title-accent">Cutlery Set</span></h2>
      </div>
      <p class="brand-name">Verdalo</p>
      <div class="bamboo-field">
        <svg viewBox="0 0 205 300" preserveAspectRatio="none" role="img" aria-label="Bamboo stalks with cutlery silhouettes rising among leaves">
          <defs><linearGradient id="fieldD" x1="0" y1="0" x2="0" y2="1"><stop offset="0" stop-color="var(--teal)" stop-opacity="0"/><stop offset=".45" stop-color="var(--teal)"/><stop offset="1" stop-color="var(--teal)"/></linearGradient></defs>
          <rect width="205" height="300" fill="url(#fieldD)"/>
        </svg>
      </div>
    </section>

  </div>
</main>
</body>
</html>
```